Verpackungsdesign für Whiskytasting-Set
Zielgruppe
Wir sind eine familiengeführte Brennerei und benötigen ein Design für unser Whiskytasting-Set, unsere Zielgruppe sind meist Männer im mittleren Alter die gerne Genießen. Das Set wird oft als Geschenk gekauft.
Aufgabenstellung
Wir benötigen eine Banderole für unser Whiskytasting Set.
Die Box hat eine Größe von 175x115x45mm (B/H/T) - Bild ist beigefügt.
Die Banderole muss nicht die komplette Breite ausfüllen sondern kann auch schmaler sein.
Es sollte eine Überlappung von mindestens einem Centimeter mit eingeplant werden, damit wir die Banderole kleben können.
Folgende Elemente müssen zwischend auf die Banderole (Daten beigefügt):
-Barcode
-Logo
-Text: 'Whiskytastingset' oder ein anderer Hinweis darauf, dass sich im Set Whiskys befinden
Das Design soll auffallen aber nicht zu bunt werden. Am liebsten sind uns natürliche Farben (schwarz, braun, weis, beige, grün), da diese gut zum Thema passen.
Gerne mit Illustraionen zum Thema Whisky oder einem passenden Spruch.
Hier noch ein paar Infos zur Brennerei bzw. zu den Whiskys:
Alle unsere Whiskys werden in Handarbeit in kleinen Chargen hergestellt.
In der Box befinden sich insgesamt 4 Whiskys je 0,05l, zwei rauchige und zwei nichtrauchige Whiskys.
UPDATE: Wir haben uns nun für einen braunen Karton entschieden.

```html
<!DOCTYPE html>
<html lang="de">
<head>
<meta charset="utf-8">
<title>Brennholt – Whiskey Tasting Set Banderole</title>
<link rel="stylesheet" href="https://fonts.googleapis.com/css2?family=Rye&display=swap">
<style>
  :root {
    --page-bg: #f2efe9;
    --kraft: #c9a57a;
    --kraft-dark: #b08c60;
    --ink: #1e1712;
    --ink-soft: #3a2d22;
    --copper: #d08a2e;
    --copper-deep: #8a4e16;
    --grey-art: #7d7468;
  }
  * { box-sizing: border-box; margin: 0; padding: 0; }
  html, body {
    width: 1200px;
    height: 1200px;
    overflow: hidden;
    background: var(--page-bg);
  }
  .canvas {
    width: 1200px;
    height: 1200px;
    display: flex;
    align-items: center;
    justify-content: center;
  }
  .label {
    position: relative;
    width: 1100px;
    height: 723px;
    background: var(--kraft);
    font-family: "Rye", serif;
    color: var(--ink);
  }
  .label-frame {
    position: absolute;
    inset: 22px;
    border: 3px solid var(--ink-soft);
    outline: 1px solid var(--ink-soft);
    outline-offset: 6px;
  }
  .still-art {
    position: absolute;
    left: 50%;
    top: 70px;
    width: 230px;
    height: 190px;
    transform: translateX(-50%);
    border-radius: 50% 50% 12px 12px;
    background: radial-gradient(circle at 55% 45%, var(--copper) 0%, var(--copper-deep) 80%);
  }
  .brand {
    position: absolute;
    left: 0;
    right: 0;
    top: 262px;
    text-align: center;
    font-size: 104px;
    letter-spacing: 4px;
    line-height: 1;
    color: var(--ink);
  }
  .tagline {
    position: absolute;
    left: 0;
    right: 0;
    top: 386px;
    text-align: center;
    font-size: 27px;
    letter-spacing: 1px;
    color: var(--ink);
  }
  .set-row {
    position: absolute;
    left: 0;
    right: 0;
    top: 440px;
    display: flex;
    align-items: center;
    justify-content: center;
    gap: 60px;
  }
  .barrel-art {
    width: 150px;
    height: 110px;
    border-radius: 40px;
    background: linear-gradient(180deg, #9a9084, var(--grey-art));
  }
  .glass-art {
    width: 110px;
    height: 110px;
    border-radius: 14px;
    background: linear-gradient(180deg, #9a9084, var(--grey-art));
  }
  .bottle-count {
    text-align: center;
    line-height: 1;
  }
  .bottle-count .number { display: block; font-size: 34px; }
  .bottle-count .word { display: block; font-size: 44px; letter-spacing: 2px; margin-top: 6px; }
  .set-title {
    position: absolute;
    left: 0;
    right: 0;
    top: 585px;
    text-align: center;
    font-size: 26px;
    letter-spacing: 10px;
    color: var(--ink);
  }
</style>
</head>
<body>
  <main class="canvas">
    <section class="label">
      <div class="label-frame"></div>
      <div class="still-art" role="img" aria-label="Illustration einer kupfernen Brennblase"></div>
      <h1 class="brand">BRENNHOLT</h1>
      <p class="tagline">WHISKY, GIN UND EDELDESTILLATE AUS KARLSRUHE</p>
      <div class="set-row">
        <div class="barrel-art" role="img" aria-label="Illustration liegender Whiskyfässer"></div>
        <p class="bottle-count"><span class="number">4</span><span class="word">BOTTLES</span></p>
        <div class="glass-art" role="img" aria-label="Illustration eines Whiskyglases mit Eis"></div>
      </div>
      <p class="set-title">WHISKEY TASTING SET</p>
    </section>
  </main>
</body>
</html>
```